Bright Fern Custom Homes business card. Double sided. Modern. professional

Bright Fern Custom Homes
contemporary modern design with our logo /
Double sided with all our contact information
Use same Green colors as in our Logo. Contemporary logo that grabs your attention. Visually pleasing and balanced. Easy to read, and Vibrant. Would love an option for rounded edges. Embossed logo would be amazing.
Contact Information for Business Card
Dana Welk Owner / General Contractor Bright Fern Custom Homes p: 704.552.1830 m: 912.648.2071 e: brightferncustomhomes@mailbox.example w: www.brightferncustomhomes.example 218 Pryor Meadow Lane Batesburg, SC 29041

```html
<!DOCTYPE html>
<html lang="en">
<head>
<meta charset="utf-8">
<title>Bright Fern Custom Homes – Business Card</title>
<link rel="stylesheet" href="https://fonts.googleapis.com/css2?family=Outfit:wght@300;400;600;700&display=swap">
<style>
  :root {
    --page-bg: #ffffff;
    --card-light: #e9eadf;
    --card-green: #738c38;
    --leaf-dark: #5b7a2e;
    --ink-light: #eef0e4;
  }
  html, body {
    margin: 0;
    padding: 0;
    width: 949px;
    height: 1200px;
    overflow: hidden;
    background: var(--page-bg);
    font-family: "Outfit", sans-serif;
  }
  .canvas {
    position: relative;
    width: 949px;
    height: 1200px;
  }
  .card {
    position: absolute;
    left: 92px;
    width: 757px;
    height: 463px;
    box-sizing: border-box;
  }
  .card-front {
    top: 91px;
    background: var(--card-light);
  }
  .card-back {
    top: 628px;
    background: var(--card-green);
    color: var(--ink-light);
    text-align: center;
  }
  .brand {
    position: absolute;
    left: 0;
    right: 0;
    display: flex;
    flex-direction: column;
    align-items: center;
  }
  .brand-front {
    top: 150px;
    color: var(--leaf-dark);
  }
  .brand-back {
    top: 34px;
    color: var(--ink-light);
  }
  .brand-mark {
    border-radius: 50%;
    background: currentColor;
  }
  .brand-front .brand-mark { width: 100px; height: 100px; margin-bottom: 46px; }
  .brand-back .brand-mark { width: 44px; height: 44px; margin-bottom: 14px; }
  .brand-name {
    font-weight: 400;
    text-transform: uppercase;
    letter-spacing: 0.08em;
    white-space: nowrap;
    line-height: 1;
  }
  .brand-front .brand-name { font-size: 28px; }
  .brand-back .brand-name { font-size: 12px; }
  .person {
    position: absolute;
    top: 182px;
    left: 0;
    right: 0;
  }
  .person-name {
    margin: 0;
    font-size: 34px;
    font-weight: 700;
    letter-spacing: 0.07em;
    line-height: 1;
  }
  .person-role {
    margin: 6px 0 0;
    font-size: 13.5px;
    font-weight: 300;
    text-transform: uppercase;
    line-height: 1;
  }
  .divider {
    position: absolute;
    top: 275px;
    left: 238px;
    width: 280px;
    border-top: 1px dashed var(--ink-light);
  }
  .contact {
    position: absolute;
    top: 312px;
    left: 0;
    right: 0;
    margin: 0;
    padding: 0;
    list-style: none;
    font-size: 16.5px;
    font-weight: 300;
    line-height: 25.5px;
  }
</style>
</head>
<body>
<main class="canvas">
  <section class="card card-front" aria-label="Card front">
    <div class="brand brand-front">
      <span class="brand-mark" aria-hidden="true"></span>
      <span class="brand-name">Bright Fern Custom Homes</span>
    </div>
  </section>

  <section class="card card-back" aria-label="Card back">
    <div class="brand brand-back">
      <span class="brand-mark" aria-hidden="true"></span>
      <span class="brand-name">Bright Fern Custom Homes</span>
    </div>
    <div class="person">
      <h1 class="person-name">DANA WELK</h1>
      <p class="person-role">Owner / General Contractor</p>
    </div>
    <div class="divider"></div>
    <ul class="contact">
      <li>704 552 1830, 912 648 2071</li>
      <li>brightferncustomhomes@mailbox.example</li>
      <li>www.brightferncustomhomes.example</li>
      <li>218 Pryor Meadow Lane Alder Ridge, NC 29041</li>
    </ul>
  </section>
</main>
</body>
</html>
```